business card for LWR pty ltd

We require a business card that stands out . I have included our company flyer and would like the services listed to be put on the card so when we Give out the cards to customers they have an idea of services we provide. need the winning design to be in editable photo shop format, editable iMac pages format or editable windows publisher format, so that I can enter in names, email addresses, phone numbers etc myself. I have included a pdf documents of info / items needed on the card to use as reference please.
Updates

need more submissions

Need extra days to review

Sick

Target Market(s)

new customers

Contact Information for Business Card

details are on attached business card requirements file

Requirements
Must have
• I have attached a list of must haves

```html
<!DOCTYPE html>
<html lang="en">
<head>
<meta charset="utf-8">
<title>LWR Pty Ltd – Business Card</title>
<link rel="stylesheet" href="https://fonts.googleapis.com/css2?family=Roboto:wght@400;500;700;900&family=Exo+2:ital,wght@1,800&display=swap">
<style>
  :root {
    --backdrop: #3a3a3a;
    --card: #050505;
    --panel: #111111;
    --silver: #c9c9c9;
    --silver-dark: #8a8a8a;
    --white: #f2f2f2;
    --gold: #a88a55;
    --gold-light: #c9a86a;
    --earth: #a9754a;
    --earth-dark: #3b2a1d;
  }
  * { box-sizing: border-box; margin: 0; padding: 0; }
  html, body { width: 1200px; height: 976px; overflow: hidden; }
  body {
    background: var(--backdrop);
    font-family: "Roboto", Arial, sans-serif;
    position: relative;
  }
  .card {
    position: absolute;
    width: 700px;
    height: 400px;
    background: var(--card);
    overflow: hidden;
    box-shadow: 0 14px 30px rgba(0,0,0,.55);
  }
  .card--services { left: 90px; top: 60px; }
  .card--contact { left: 410px; top: 516px; }

  .mesh {
    position: absolute;
    background: radial-gradient(ellipse at 50% 45%, #3d3d3d 0%, #1c1c1c 55%, #070707 100%);
  }
  .brand-name {
    position: absolute;
    font-family: "Roboto", Arial, sans-serif;
    font-weight: 900;
    color: var(--silver);
    letter-spacing: 4px;
    line-height: 1;
  }
  .brand-name::after {
    content: "";
    display: inline-block;
    width: .22em; height: .22em;
    background: var(--silver);
    border-radius: 50%;
    margin-left: .12em;
    vertical-align: top;
  }

  /* services side */
  .card--services .mesh { left: 150px; top: 0; width: 260px; height: 240px; }
  .card--services .brand-name { left: 175px; top: 55px; font-size: 96px; }
  .truck-photo {
    position: absolute;
    left: 0; top: 170px;
    width: 700px; height: 110px;
    background: linear-gradient(180deg, var(--earth-dark) 0%, var(--earth) 60%, #7d5535 100%);
    clip-path: polygon(0 35%, 60% 0, 100% 0, 100% 35%, 60% 100%, 0 100%);
  }
  .services-tab {
    position: absolute;
    left: 250px; top: 238px;
    background: var(--gold);
    color: var(--white);
    font-family: "Exo 2", sans-serif;
    font-style: italic;
    font-weight: 800;
    font-size: 17px;
    padding: 5px 26px 5px 18px;
    clip-path: polygon(0 0, 90% 0, 100% 100%, 0 100%);
  }
  .services-list {
    position: absolute;
    left: 28px; right: 24px; top: 288px;
    color: var(--white);
    font-size: 16px;
    line-height: 1.55;
  }
  .services-list .dot { color: var(--gold-light); margin: 0 5px; }

  /* contact side */
  .card--contact .mesh { left: 170px; top: 0; width: 380px; height: 250px; }
  .card--contact .brand-name { left: 205px; top: 70px; font-size: 110px; }
  .silver-rule {
    position: absolute; left: 0; top: 250px;
    width: 100%; height: 3px;
    background: linear-gradient(90deg, #666, var(--silver), #777);
  }
  .name-block {
    position: absolute; left: 30px; top: 285px; width: 330px;
    text-align: right;
  }
  .person-name {
    font-weight: 900; font-size: 34px; color: var(--silver);
    letter-spacing: 1px;
  }
  .person-role { font-size: 20px; color: var(--silver-dark); margin-top: 2px; }
  .divider {
    position: absolute; left: 385px; top: 268px;
    width: 1px; height: 115px; background: #3a3a3a;
  }
  .contact-block {
    position: absolute; left: 405px; top: 270px;
    color: var(--white); font-size: 14px; line-height: 1.45;
  }
  .company { font-weight: 700; font-size: 18px; }
  .contact-row { display: flex; align-items: center; gap: 7px; }
  .contact-row svg { width: 12px; height: 12px; fill: none; stroke: var(--silver); stroke-width: 1.6; }
  .gap { height: 8px; }
</style>
</head>
<body>

<section class="card card--services">
  <div class="mesh" role="img" aria-label="Dark metallic honeycomb mesh texture"></div>
  <div class="truck-photo" role="img" aria-label="Photo of a road train with tipper trailers on a red dirt road"></div>
  <div class="brand-name">LWR</div>
  <div class="services-tab">OUR SERVICES</div>
  <p class="services-list">
    <span class="dot">•</span>Over size loads / Hot Shot Loads <span class="dot">•</span>Heavy Vehicle Recovery services <span class="dot">•</span>Potable Water Deliveries <span class="dot">•</span>Road Building / Maintenance <span class="dot">•</span>Earthworks <span class="dot">•</span>Sand &amp; Metal Supply &amp; Cartage <span class="dot">•</span>Road Train Tippers <span class="dot">•</span>Road Train Tankers <span class="dot">•</span>Road Train Flat Tops <span class="dot">•</span>Drop Deck Trailers <span class="dot">•</span>Mine site accredited <span class="dot">•</span>Equipment &amp; Operators
  </p>
</section>

<section class="card card--contact">
  <div class="mesh" role="img" aria-label="Dark metallic honeycomb mesh texture"></div>
  <div class="brand-name">LWR</div>
  <div class="silver-rule"></div>
  <div class="name-block">
    <div class="person-name">DANIEL FRASER</div>
    <div class="person-role">Director</div>
  </div>
  <div class="divider"></div>
  <div class="contact-block">
    <div class="company">LWR Pty Ltd</div>
    <div>Lot 12 example road Australia</div>
    <div class="gap"></div>
    <div class="contact-row">
      <svg viewBox="0 0 12 12"><path d="M2 1l2 0 1 3-1.5 1a6 6 0 0 0 3.5 3.5L8 7l3 1v2a1 1 0 0 1-1 1A9 9 0 0 1 1 2a1 1 0 0 1 1-1z"/></svg>
      <span>000 555 000</span>
    </div>
    <div class="contact-row">
      <svg viewBox="0 0 12 12"><rect x="1" y="2.5" width="10" height="7"/><path d="M1 2.5l5 4 5-4"/></svg>
      <span>info@lwrservices.com.au</span>
    </div>
    <div class="contact-row">
      <svg viewBox="0 0 12 12"><circle cx="6" cy="6" r="5"/><path d="M1 6h10M6 1c-3 3-3 7 0 10M6 1c3 3 3 7 0 10"/></svg>
      <span>www.lwrservices.com</span>
    </div>
  </div>
</section>

</body>
</html>
```